UX Design for Analytics Web Application

http://torvikgrove.com/
We are tech & consulting company with analytics products (web applications), located at Rio de Janeiro, Brazil.

We are searching a partner do develop UX for our products, i.e, aesthetics, usability, HTML/CSS.

Currently we have a product suite and the goal is to make a pilot re-design project with one of our products.

The product of interest is interactive webapp that aims at data analysis, significantly different from blogs, e-commerce or landing pages.

We do have a software development team but we lack an UX & HTML expert. Currently we use Bootstrap templates but the results are insatisfatory.

So, the project scope is, to develop the arts (UX, aesthetics, etc) along with the code/mockup (HTML/CSS) for one of our product (3 pages).

This is a pilot project and there's potential to rehire for our other products. Code quality is of importance.

More details and specification can be found in attached files.

Target Market(s)

Executives, managers & consultants

Industry/Entity Type

It Company

Coding

Coded - Design and coding required

Number of Pages Required

3 page

Font styles to use
Sans Serif

Requirements
Must have
• (see attached files, prefer the pptx version))
• -Responsive
Nice to have
• (see attached files, prefer the pptx version)
Should not have
• -Avoid Green, Red and Yellow colors. They have a meaning of good, bad and average in our products.

```html
<!DOCTYPE html>
<html lang="en">
<head>
<meta charset="utf-8">
<title>Torvik Grove · Dashboard</title>
<link href="https://fonts.googleapis.com/css2?family=Open+Sans:wght@400;600;700&display=swap" rel="stylesheet">
<style>
:root{
  --ink:#2b2b2b;
  --sidebar:#3a3a3a;
  --sidebar-active:#2c2c2c;
  --navy:#1f2b5e;
  --navy-deep:#1b2552;
  --feed:#1d2231;
  --feed-item:#3f4b60;
  --teal:#2ab3c8;
  --cyan:#5ad8f0;
  --purple:#a35ae6;
  --grey-ring:#dcdcdc;
  --tab:#d3d3d3;
  --card:#f1f1f1;
  --slate:#3d4a63;
  --footer:#ececec;
}
*{box-sizing:border-box;margin:0;padding:0}
html,body{width:930px;height:1200px;overflow:hidden;background:#fff;font-family:"Open Sans",sans-serif;color:var(--ink)}
.app{position:relative;width:930px;height:1200px;overflow:hidden}

.topbar{position:absolute;left:0;top:0;width:930px;height:99px;border-bottom:1px solid #ddd;background:#fff}
.menu-toggle{position:absolute;left:19px;top:40px;width:22px}
.menu-toggle span{display:block;height:3px;background:#333;margin-bottom:5px;border-radius:1px}
.brand-name{position:absolute;left:104px;top:26px;font-size:32px;font-weight:700;color:#333;white-space:nowrap;line-height:40px}
.top-icon{position:absolute;top:34px;width:32px;height:32px;border-radius:50%;background:#333;display:flex;align-items:center;justify-content:center}
.top-icon svg{width:14px;height:14px;fill:#fff}
.badge-count{position:absolute;left:-8px;top:-6px;width:16px;height:16px;border-radius:50%;background:var(--cyan);color:#fff;font-size:8px;display:flex;align-items:center;justify-content:center}

.sidebar{position:absolute;left:0;top:99px;width:198px;height:1057px;background:var(--sidebar);z-index:5}
.nav-item{display:flex;align-items:center;height:43px;padding-left:18px;color:#fff;font-size:14px}
.nav-item.active{background:var(--sidebar-active)}
.nav-item svg{width:10px;height:10px;fill:#fff;margin-right:12px}

.stats{position:absolute;left:120px;top:113px;width:339px;height:297px;background:var(--navy-deep);color:#fff;overflow:hidden}
.stats-top{height:161px;background:var(--navy);position:relative}
.stats-count{position:absolute;left:-8px;top:14px;font-size:84px;font-weight:700;line-height:92px}
.stats-label{position:absolute;left:56px;top:108px;font-size:18px}
.stats-ring{position:absolute;left:218px;top:22px;width:88px;height:88px}
.stats-pct{position:absolute;left:202px;top:112px;font-size:13px;white-space:nowrap}
.stats-pct b{font-size:24px;font-weight:700;margin-right:4px}
.metric{position:absolute;left:34px;font-size:18px;white-space:nowrap}
.metric-bar{position:absolute;left:204px;height:12px}
.metric-val{position:absolute;font-size:13px;font-weight:700}

.feed{position:absolute;left:120px;top:423px;width:339px;height:298px;background:var(--feed);overflow:hidden}
.feed-item{position:absolute;left:0;width:326px;background:var(--feed-item);color:#fff;font-size:10.5px;line-height:14px;padding:14px 10px 0 74px}
.feed-item .who{color:var(--cyan)}
.feed-item .proc{color:#c59af0}
.feed-item time{display:block;font-size:8px;color:#c8ccd4;margin-top:4px}
.see-all{position:absolute;left:130px;top:248px;width:63px;height:32px;border:1px solid #6b7385;color:#c9ccd3;font-size:10px;display:flex;align-items:center;justify-content:center}

.tabs{position:absolute;left:471px;top:113px;width:356px;height:40px;border-bottom:3px solid var(--cyan)}
.tab{position:absolute;top:0;width:87px;height:37px;display:flex;align-items:center;justify-content:center;font-size:10.5px;color:#555;background:var(--tab)}
.tab svg{width:9px;height:9px;margin-right:5px;fill:currentColor}
.tab.active{background:var(--teal);color:#fff}

.card{position:absolute;width:173px;height:174px;background:var(--card)}
.card-photo{position:relative;height:80px;overflow:hidden}
.card-title{position:absolute;left:0;top:59px;width:100%;height:21px;background:rgba(60,60,60,.65);color:#fff;font-size:10px;font-weight:700;padding:4px 13px;letter-spacing:.2px}
.card-tools{position:absolute;right:2px;top:2px;display:flex;flex-direction:column;gap:8px}
.tool{width:14px;height:14px;display:flex;align-items:center;justify-content:center;background:rgba(40,40,40,.7)}
.tool svg{width:9px;height:9px;fill:none;stroke:#fff;stroke-width:1.6}
.tool.ok{background:var(--teal)}
.tool.cfg{background:var(--purple)}
.card-amount{position:absolute;left:14px;top:98px;font-size:9.5px;line-height:11px;color:#1e2a4a;width:80px;padding-left:12px}
.card-amount svg{position:absolute;left:0;top:0;width:8px;height:9px;fill:#1e2a4a}
.card-note{position:absolute;left:14px;top:126px;width:93px;font-size:7.2px;line-height:11px;color:#777}
.card-ring{position:absolute;left:107px;top:100px;width:56px;height:56px}

.new-process{position:absolute;left:471px;top:1094px;width:356px;height:36px;background:var(--slate);color:#fff;font-size:12.5px;display:flex;align-items:center;justify-content:center}
.new-process svg{width:10px;height:10px;margin-right:5px}

.footer{position:absolute;left:0;top:1156px;width:930px;height:44px;background:var(--footer);font-size:8px;color:#444}
.footer p{position:absolute;left:360px;top:17px}
.footer span{position:absolute;right:10px;top:26px}
</style>
</head>
<body>
<svg width="0" height="0" style="position:absolute">
  <defs>
    <symbol id="ring" viewBox="0 0 60 60">
      <circle cx="30" cy="30" r="24" fill="none" stroke="var(--grey-ring)" stroke-width="9"/>
      <circle cx="30" cy="30" r="24" fill="none" stroke="var(--teal)" stroke-width="9" stroke-dasharray="108 200" transform="rotate(-90 30 30)"/>
      <circle cx="30" cy="30" r="24" fill="none" stroke="var(--purple)" stroke-width="9" stroke-dasharray="32 200" transform="rotate(170 30 30)"/>
    </symbol>
    <symbol id="tick" viewBox="0 0 10 10"><circle cx="5" cy="5" r="4"/><path d="M3 5l1.5 1.5L7 3.7"/></symbol>
    <symbol id="cog" viewBox="0 0 10 10"><circle cx="5" cy="5" r="2"/><path d="M5 0.8v1.5M5 7.7v1.5M0.8 5h1.5M7.7 5h1.5M2 2l1 1M7 7l1 1M8 2l-1 1M3 7l-1 1"/></symbol>
    <symbol id="ban" viewBox="0 0 10 10"><circle cx="5" cy="5" r="4"/><path d="M2.2 7.8l5.6-5.6"/></symbol>
    <symbol id="bin" viewBox="0 0 10 10"><path d="M2 2.5h6M4 2.5V1.5h2v1M3 2.5v6h4v-6"/></symbol>
    <symbol id="up" viewBox="0 0 8 9"><path d="M4 0L8 4H5V9H3V4H0z"/></symbol>
  </defs>
</svg>

<div class="app">
  <header class="topbar">
    <div class="menu-toggle"><span></span><span></span><span></span></div>
    <div class="brand-name">Torvik Grove</div>
    <div class="top-icon" style="left:684px"><span class="badge-count">0</span><svg viewBox="0 0 10 10"><path d="M5 1a3 3 0 0 1 3 3v3l1 1H1l1-1V4a3 3 0 0 1 3-3zM4 9h2a1 1 0 0 1-2 0z"/></svg></div>
    <div class="top-icon" style="left:740px"><svg viewBox="0 0 10 10"><circle cx="5" cy="3" r="2.2"/><path d="M1 10c0-3 2-4.5 4-4.5S9 7 9 10z"/></svg></div>
    <div class="top-icon" style="left:796px"><svg viewBox="0 0 10 10"><path d="M4 0h2l.3 1.5 1.3.6L9 1.3l1 1.7-1.1 1.1v1.8L10 7l-1 1.7-1.4-.8-1.3.6L6 10H4l-.3-1.5-1.3-.6L1 8.7 0 7l1.1-1.1V4.1L0 3l1-1.7 1.4.8 1.3-.6z"/><circle cx="5" cy="5" r="1.6" fill="#333"/></svg></div>
  </header>

  <nav class="sidebar">
    <div class="nav-item active"><svg viewBox="0 0 10 10"><path d="M5 0l5 5H8.5v5H6V7H4v3H1.5V5H0z"/></svg>Dashboard</div>
    <div class="nav-item"><svg viewBox="0 0 10 10"><path d="M5 1a4 4 0 0 1 3.5 2L10 2v4H6l1.6-1.4A2.5 2.5 0 0 0 2.5 5H1a4 4 0 0 1 4-4zM0 6h4L2.4 7.4A2.5 2.5 0 0 0 7.5 7H9a4 4 0 0 1-7.5 2L0 10z"/></svg>Process</div>
    <div class="nav-item"><svg viewBox="0 0 10 10"><path d="M0 0h1v9h9v1H0zM2 5h1.5v3H2zM4.5 2H6v6H4.5zM7 4h1.5v4H7z"/></svg>Results</div>
    <div class="nav-item"><svg viewBox="0 0 10 10"><circle cx="5" cy="3" r="2.5"/><path d="M1 10c0-3 2-4.5 4-4.5S9 7 9 10z"/></svg>Profile</div>
    <div class="nav-item"><svg viewBox="0 0 10 10"><path d="M5 0.5a3 3 0 0 1 3 3v3l1.2 1.3H0.8L2 6.5v-3a3 3 0 0 1 3-3zM4 8.6h2a1 1 0 0 1-2 0z"/></svg>Notifications</div>
    <div class="nav-item"><svg viewBox="0 0 10 10"><path d="M4 0h2l.3 1.5 1.3.6L9 1.3l1 1.7-1.1 1.1v1.8L10 7l-1 1.7-1.4-.8-1.3.6L6 10H4l-.3-1.5-1.3-.6L1 8.7 0 7l1.1-1.1V4.1L0 3l1-1.7 1.4.8 1.3-.6z"/><circle cx="5" cy="5" r="1.6" fill="#3a3a3a"/></svg>Configurations</div>
  </nav>

  <section class="stats">
    <div class="stats-top">
      <div class="stats-count">24</div>
      <div class="stats-label">Processes</div>
      <svg class="stats-ring" viewBox="0 0 60 60" aria-hidden="true"><use href="#ring"/></svg>
      <div class="stats-pct"><b>72%</b>Concluded</div>
    </div>
    <div class="metric" style="top:186px">Millions Expent</div>
    <div class="metric-bar" style="top:194px;width:110px;background:var(--teal)"></div>
    <div class="metric" style="top:219px">Millions of gap</div>
    <div class="metric-bar" style="top:227px;width:48px;background:var(--purple)"></div>
    <div class="metric-val" style="left:260px;top:224px">6%</div>
    <div class="metric" style="top:251px">Million negotiated</div>
    <div class="metric-bar" style="top:259px;width:35px;background:#ddd"></div>
    <div class="metric-val" style="left:246px;top:256px">5%</div>
  </section>

  <section class="feed">
    <div class="feed-item" style="top:13px;height:68px"><span class="who">John Smith</span> upload new data with 23823 rows to the <span class="proc">KPTO Process</span> and he is happy now<time>2 days ago</time></div>
    <div class="feed-item" style="top:88px;height:68px"><span class="who">Daisy Jr</span> Donec non eros sodales tristique<time>3 days ago</time></div>
    <div class="feed-item" style="top:163px;height:68px"><span class="who">Andre Santos</span> Integer cursus justo orci, lacinia ultrices nisi elementum vitae<time>4 days ago</time></div>
    <div class="see-all">Sell All</div>
  </section>

  <div class="tabs">
    <div class="tab active" style="left:0"><svg viewBox="0 0 10 10"><path d="M4 0a4 4 0 0 1 3.2 6.4L10 9.2 9.2 10 6.4 7.2A4 4 0 1 1 4 0zm0 1.5a2.5 2.5 0 1 0 0 5 2.5 2.5 0 0 0 0-5z"/></svg>Search</div>
    <div class="tab" style="left:90px"><svg viewBox="0 0 10 10"><path d="M0 1h2v2H0zM3 1h7v2H3zM0 4h2v2H0zM3 4h7v2H3zM0 7h2v2H0zM3 7h7v2H3z"/></svg>Sort by</div>
    <div class="tab" style="left:180px"><svg viewBox="0 0 10 10"><path d="M0 0h10L6 5v5L4 9V5z"/></svg>Filter by</div>
  </div>

  <article class="card" style="left:471px;top:163px">
    <div class="card-photo" role="img" aria-label="Photo of laptops on a meeting table" style="background:linear-gradient(135deg,#6d625a,#b8b0a6 60%,#4a4744)"></div>
    <div class="card-title">PROCESS BY DONUT</div>
    <div class="card-tools"><span class="tool ok"><svg><use href="#tick"/></svg></span><span class="tool"><svg><use href="#bin"/></svg></span></div>
    <div class="card-amount"><svg><use href="#up"/></svg>14 million in expenses</div>
    <p class="card-note">Nulla a ultricies, malesuada rhoncus eget. Suspendisse erat, dictum.</p>
    <svg class="card-ring" viewBox="0 0 60 60" aria-hidden="true"><use href="#ring"/></svg>
  </article>
  <article class="card" style="left:655px;top:163px">
    <div class="card-photo" role="img" aria-label="Photo of printed charts on a desk" style="background:linear-gradient(135deg,#dfe4ea,#a9b8cb 55%,#7d8793)"></div>
    <div class="card-title">PROCESS BY DONUT</div>
    <div class="card-tools"><span class="tool cfg"><svg><use href="#cog"/></svg></span><span class="tool"><svg><use href="#bin"/></svg></span></div>
    <div class="card-amount"><svg><use href="#up"/></svg>14 million in expenses</div>
    <p class="card-note">Nulla a ultricies, malesuada rhoncus eget. Suspendisse erat, dictum.</p>
    <svg class="card-ring" viewBox="0 0 60 60" aria-hidden="true"><use href="#ring"/></svg>
  </article>

  <article class="card" style="left:471px;top:349px">
    <div class="card-photo" role="img" aria-label="Photo of a hand pointing at a report" style="background:linear-gradient(135deg,#3c5568,#9fb6c4 60%,#d9e2e8)"></div>
    <div class="card-title">PROCESS BY DONUT</div>
    <div class="card-tools"><span class="tool cfg"><svg><use href="#cog"/></svg></span><span class="tool"><svg><use href="#bin"/></svg></span></div>
    <div class="card-amount"><svg><use href="#up"/></svg>14 million in expenses</div>
    <p class="card-note">Nulla a ultricies, malesuada rhoncus eget. Suspendisse erat, dictum.</p>
    <svg class="card-ring" viewBox="0 0 60 60" aria-hidden="true"><use href="#ring"/></svg>
  </article>
  <article class="card" style="left:655px;top:349px">
    <div class="card-photo" role="img" aria-label="Photo of a tablet showing a dashboard" style="background:linear-gradient(135deg,#2f2f2f,#8a8580 55%,#d6d2cc)"></div>
    <div class="card-title">PROCESS BY DONUT</div>
    <div class="card-tools"><span class="tool"><svg><use href="#ban"/></svg></span><span class="tool"><svg><use href="#bin"/></svg></span></div>
    <div class="card-amount"><svg><use href="#up"/></svg>14 million in expenses</div>
    <p class="card-note">Nulla a ultricies, malesuada rhoncus eget. Suspendisse erat, dictum.</p>
    <svg class="card-ring" viewBox="0 0 60 60" aria-hidden="true"><use href="#ring"/></svg>
  </article>

  <article class="card" style="left:471px;top:535px">
    <div class="card-photo" role="img" aria-label="Photo of hands holding a tablet with charts" style="background:linear-gradient(135deg,#2a2524,#56677a 55%,#1e2126)"></div>
    <div class="card-title">PROCESS BY DONUT</div>
    <div class="card-tools"><span class="tool ok"><svg><use href="#tick"/></svg></span><span class="tool"><svg><use href="#bin"/></svg></span></div>
    <div class="card-amount"><svg><use href="#up"/></svg>14 million in expenses</div>
    <p class="card-note">Nulla a ultricies, malesuada rhoncus eget. Suspendisse erat, dictum.</p>
    <svg class="card-ring" viewBox="0 0 60 60" aria-hidden="true"><use href="#ring"/></svg>
  </article>
  <article class="card" style="left:655px;top:535px">
    <div class="card-photo" role="img" aria-label="Photo of a business team" style="background:linear-gradient(135deg,#e8e8e8,#7b7b80 55%,#3a3a40)"></div>
    <div class="card-title">PROCESS BY DONUT</div>
    <div class="card-tools"><span class="tool cfg"><svg><use href="#cog"/></svg></span><span class="tool"><svg><use href="#bin"/></svg></span></div>
    <div class="card-amount"><svg><use href="#up"/></svg>14 million in expenses</div>
    <p class="card-note">Nulla a ultricies, malesuada rhoncus eget. Suspendisse erat, dictum.</p>
    <svg class="card-ring" viewBox="0 0 60 60" aria-hidden="true"><use href="#ring"/></svg>
  </article>

  <article class="card" style="left:471px;top:721px">
    <div class="card-photo" role="img" aria-label="Illustration of blue financial charts under a magnifier" style="background:linear-gradient(135deg,#7fb0e6,#2f6fc2 55%,#133a7a)"></div>
    <div class="card-title">PROCESS BY DONUT</div>
    <div class="card-tools"><span class="tool"><svg><use href="#ban"/></svg></span><span class="tool"><svg><use href="#bin"/></svg></span></div>
    <div class="card-amount"><svg><use href="#up"/></svg>14 million in expenses</div>
    <p class="card-note">Nulla a ultricies, malesuada rhoncus eget. Suspendisse erat, dictum.</p>
    <svg class="card-ring" viewBox="0 0 60 60" aria-hidden="true"><use href="#ring"/></svg>
  </article>
  <article class="card" style="left:655px;top:721px">
    <div class="card-photo" role="img" aria-label="Photo of people reviewing papers on a dark table" style="background:linear-gradient(135deg,#1c1c1c,#5a5552 55%,#bfb8b0)"></div>
    <div class="card-title">PROCESS BY DONUT</div>
    <div class="card-tools"><span class="tool ok"><svg><use href="#tick"/></svg></span><span class="tool"><svg><use href="#bin"/></svg></span></div>
    <div class="card-amount"><svg><use href="#up"/></svg>14 million in expenses</div>
    <p class="card-note">Nulla a ultricies, malesuada rhoncus eget. Suspendisse erat, dictum.</p>
    <svg class="card-ring" viewBox="0 0 60 60" aria-hidden="true"><use href="#ring"/></svg>
  </article>

  <article class="card" style="left:471px;top:907px">
    <div class="card-photo" role="img" aria-label="Photo of a laptop showing a stock chart" style="background:linear-gradient(135deg,#f0f0f0,#a7a7a7 55%,#4c4c4c)"></div>
    <div class="card-title">PROCESS BY DONUT</div>
    <div class="card-tools"><span class="tool ok"><svg><use href="#tick"/></svg></span><span class="tool"><svg><use href="#bin"/></svg></span></div>
    <div class="card-amount"><svg><use href="#up"/></svg>14 million in expenses</div>
    <p class="card-note">Nulla a ultricies, malesuada rhoncus eget. Suspendisse erat, dictum.</p>
    <svg class="card-ring" viewBox="0 0 60 60" aria-hidden="true"><use href="#ring"/></svg>
  </article>
  <article class="card" style="left:655px;top:907px">
    <div class="card-photo" role="img" aria-label="Photo of glasses resting on blue bar charts" style="background:linear-gradient(135deg,#1e3c6e,#6d93c9 55%,#c9d7ea)"></div>
    <div class="card-title">PROCESS BY DONUT</div>
    <div class="card-tools"><span class="tool ok"><svg><use href="#tick"/></svg></span><span class="tool"><svg><use href="#bin"/></svg></span></div>
    <div class="card-amount"><svg><use href="#up"/></svg>14 million in expenses</div>
    <p class="card-note">Nulla a ultricies, malesuada rhoncus eget. Suspendisse erat, dictum.</p>
    <svg class="card-ring" viewBox="0 0 60 60" aria-hidden="true"><use href="#ring"/></svg>
  </article>

  <div class="new-process"><svg viewBox="0 0 10 10"><circle cx="5" cy="5" r="5" fill="#fff"/><path d="M5 2.5v5M2.5 5h5" stroke="#3d4a63" stroke-width="1.6"/></svg>New Process</div>

  <footer class="footer">
    <p>Copyright © 2017 Company name. All rights reserved.</p>
    <span>M2</span>
  </footer>
</div>
</body>
</html>
```